Marvel Brookworks highend custom homes

We build high end custom homes and timber frames we specialize in rustic hand made designs along with iron and concrete accents to add a modern touch 90% of my homes are buit on lake front properries attached is my logo and slogan as of now and my previous one

Target Market(s)

High end custom homes

Industry/Entity Type

Custom residential construction

Contact Information for Business Card

Been in buissness 8+ years inssured and reliable

Colors
A7469A
B969AE
D3A5CF
EDDBEB
F8F0F9

Requirements
Must have
• Must have slogan and phone number
Should not have
• A combination of rustic yet modern accents

```html
<!DOCTYPE html>
<html lang="en">
<head>
<meta charset="UTF-8">
<title>Marvel Brookworks – Business Card</title>
<link href="https://fonts.googleapis.com/css2?family=Open+Sans:wght@400;700&family=Jost:wght@400&display=swap" rel="stylesheet">
<style>
  :root {
    --plum: #A7469A;
    --orchid: #B969AE;
    --blush: #D3A5CF;
    --mist: #EDDBEB;
    --paper: #FFFFFF;
    --forest: #4B5B49;
  }
  * { margin: 0; padding: 0; box-sizing: border-box; }
  html, body {
    width: 1200px; height: 1200px; overflow: hidden;
    background: var(--paper);
    font-family: "Open Sans", sans-serif;
  }
  .card {
    position: absolute;
    top: 461px;
    width: 449px; height: 288px;
    border-radius: 26px;
    overflow: hidden;
  }
  .card--front {
    left: 129px;
    background: var(--paper);
    border: 1px solid var(--blush);
  }
  .card--back {
    left: 629px;
    background: var(--plum);
  }
  .front__brand-side {
    position: absolute; left: 0; top: 0;
    width: 225px; height: 100%;
    display: flex; align-items: center; justify-content: center;
  }
  .front__info-side {
    position: absolute; left: 225px; top: 0;
    width: 224px; height: 100%;
    background: var(--plum);
  }
  .company-name {
    font-family: "Open Sans", sans-serif;
    font-weight: 700;
    text-align: center;
    line-height: 1.15;
  }
  .company-name--front { color: var(--forest); font-size: 24px; }
  .company-name--back { color: var(--blush); font-size: 30px; }
  .person__name {
    position: absolute; left: 16px; top: 552px;
    top: 91px;
    color: var(--blush);
    font-weight: 700; font-size: 19.5px;
    letter-spacing: 0.4px; white-space: nowrap;
  }
  .person__role {
    position: absolute; left: 16px; top: 117px;
    color: var(--mist);
    font-size: 15px; font-weight: 400;
  }
  .contact-list {
    position: absolute; left: 16px; top: 150px;
    list-style: none;
  }
  .contact-list__item {
    display: flex; align-items: center;
    height: 18.5px;
    color: var(--paper);
    font-size: 12.5px;
  }
  .contact-list__icon {
    width: 13px; height: 13px; margin-right: 9px;
    fill: var(--blush);
    flex: none;
  }
  .back__brand {
    position: absolute; left: 0; top: 0; width: 100%; height: 210px;
    display: flex; align-items: center; justify-content: center;
    padding-top: 40px;
  }
  .back__web {
    position: absolute; left: 27px; top: 237px;
    width: 378px;
    display: flex; align-items: center;
    color: var(--mist);
  }
  .back__rule { flex: 1; height: 1px; background: var(--mist); }
  .back__url {
    display: flex; align-items: center;
    margin: 0 7px;
    font-family: "Jost", sans-serif;
    font-size: 14px; letter-spacing: 2.6px;
  }
  .back__globe { width: 12px; height: 12px; margin-right: 8px; }
</style>
</head>
<body>

<section class="card card--front">
  <div class="front__brand-side">
    <div class="company-name company-name--front">Marvel<br>Brookworks</div>
  </div>
  <div class="front__info-side">
    <h1 class="person__name">YOUR NAME HERE</h1>
    <p class="person__role">Designation</p>
    <ul class="contact-list">
      <li class="contact-list__item">
        <svg class="contact-list__icon" viewBox="0 0 24 24"><path d="M6.6 10.8a15.2 15.2 0 0 0 6.6 6.6l2.2-2.2a1 1 0 0 1 1-.25 11.4 11.4 0 0 0 3.6.57 1 1 0 0 1 1 1V20a1 1 0 0 1-1 1A17 17 0 0 1 3 4a1 1 0 0 1 1-1h3.5a1 1 0 0 1 1 1c0 1.25.2 2.45.57 3.57a1 1 0 0 1-.25 1z"/></svg>
        +000-12345-6789
      </li>
      <li class="contact-list__item">
        <svg class="contact-list__icon" viewBox="0 0 24 24"><path d="M2 5h20v14H2z M2 5l10 8 10-8" /></svg>
        e-mail@mail.com
      </li>
      <li class="contact-list__item">
        <svg class="contact-list__icon" viewBox="0 0 24 24"><path d="M12 1a8 8 0 0 0-8 8c0 6 8 14 8 14s8-8 8-14a8 8 0 0 0-8-8zm0 11a3 3 0 1 1 0-6 3 3 0 0 1 0 6z"/></svg>
        Your Address 0123456
      </li>
    </ul>
  </div>
</section>

<section class="card card--back">
  <div class="back__brand">
    <div class="company-name company-name--back">Marvel<br>Brookworks</div>
  </div>
  <div class="back__web">
    <span class="back__rule"></span>
    <span class="back__url">
      <svg class="back__globe" viewBox="0 0 24 24" fill="none" stroke="currentColor" stroke-width="2"><circle cx="12" cy="12" r="10"/><path d="M2 12h20M12 2c3 3 3 17 0 20M12 2c-3 3-3 17 0 20M4 7h16M4 17h16"/></svg>
      www.yourweb.com
    </span>
    <span class="back__rule"></span>
  </div>
</section>

</body>
</html>
```